" Desenvolve empreendimentos imobiliários diferenciados, loteamentos no segmento de baixo, médio e alto padrao. É uma incorporadora com mais de 15 anos, porém criando uma holding e procurando um logo forte para introduzir o nome novo no mercado. "

```html
<!DOCTYPE html>
<html lang="pt-BR">
<head>
<meta charset="utf-8">
<title>Terrava – cartão de visita</title>
<link rel="stylesheet" href="https://fonts.googleapis.com/css2?family=Arimo:wght@400&display=swap">
<style>
  :root {
    --page: #ffffff;
    --stage: #656262;
    --card: #ffffff;
    --ink: #231f20;
    --green: #b4d147;
  }
  * { margin: 0; padding: 0; box-sizing: border-box; }
  html, body { width: 1200px; height: 1200px; overflow: hidden; background: var(--page); }
  body { position: relative; font-family: "Arimo", Arial, sans-serif; color: var(--ink); }
  .stage { position: absolute; left: 79px; top: 0; width: 1042px; height: 1200px; background: var(--stage); }
  .card { position: absolute; left: 144px; width: 905px; background: var(--card); }
  .card-front { top: 48px; height: 509px; }
  .card-back { top: 581px; height: 547px; overflow: hidden; }

  .brand { position: absolute; left: 0; right: 0; top: 190px; display: flex; align-items: center; justify-content: center; gap: 28px; }
  .brand-mark { width: 110px; height: 110px; background: var(--green); }
  .brand-name { font-size: 104px; font-weight: 400; letter-spacing: 2px; color: var(--ink); line-height: 1; }

  .brand-field { position: absolute; left: 0; top: 0; width: 905px; height: 547px; }
  .accent-bar { position: absolute; left: 852px; top: 115px; width: 53px; height: 163px; background: var(--green); }

  .holder { position: absolute; left: 455px; top: 103px; font-size: 42px; font-weight: 400; line-height: 1; }
  .contacts { position: absolute; left: 468px; top: 168px; list-style: none; font-size: 23px; line-height: 47px; }
  .address { position: absolute; left: 452px; top: 490px; font-size: 13px; white-space: nowrap; }
</style>
</head>
<body>
  <div class="stage"></div>

  <section class="card card-front">
    <div class="brand">
      <span class="brand-mark"></span>
      <span class="brand-name">Terrava</span>
    </div>
  </section>

  <section class="card card-back">
    <svg class="brand-field" viewBox="0 0 905 547" role="img" aria-label="Área decorativa verde com o símbolo da marca">
      <polygon points="0,240 182,163 278,307 350,547 0,547" fill="var(--green)"/>
    </svg>
    <span class="accent-bar"></span>
    <h1 class="holder">Nome|Função</h1>
    <ul class="contacts">
      <li>Telefone:(00)0000-0000</li>
      <li>Celular:(00)0000-0000</li>
      <li>Email:contato@exemplo.com.br</li>
    </ul>
    <p class="address">Endereço: Rua das Palmeiras,00 Bairro Jardim Novo Cidade Serena.</p>
  </section>
</body>
</html>
```